Hunting Ethics Organization Needs a Web Design with Logo Refresh

This project involves the creation of a website design including the homepage design, inside page design, and logo refinements. Our organization is Talveth, and we are a not-for-profit hunting ethics organization.
The focus of the new website design is to bring attention the mission of our organization, provide an overview of the areas where our organization deploys its resources to support the modern hunter, and to encourage visitors to support our organization by donating in support of the organization’s mission.
The winning design will be implemented in Wordpress by our in-house team. If you have questions about how any particular design element may translate to Wordpress, please feel free to post questions in response to this brief. In general, however, we’re more focused on the evolution and delivery of a strong overall design aesthetic – we’ll shoulder the responsibility of how we translate that design into Wordpress.
See attached design brief for full details.
Hunting
2 page

```html
<!DOCTYPE html>
<html lang="en">
<head>
<meta charset="utf-8">
<title>Talveth</title>
<link href="https://fonts.googleapis.com/css2?family=Open+Sans:wght@400;600;700;800&display=swap" rel="stylesheet">
<style>
:root{
  --gold:#a39a6a;
  --cream:#efecdb;
  --ink:#3b3b3b;
  --text:#555;
  --white:#fff;
  --footer:#4a4541;
  --footer-bottom:#3c3834;
  --footer-text:#e7e3d8;
  --send:#1f5b9a;
}
*{box-sizing:border-box;margin:0;padding:0}
html,body{width:1200px;height:3010px;overflow:hidden}
body{position:relative;font-family:'Open Sans',Arial,sans-serif;color:var(--text);background:var(--white)}

/* header */
.site-header{position:absolute;top:0;left:0;width:1200px;height:105px;background:var(--white)}
.brand-name{position:absolute;left:130px;top:30px;font-size:34px;font-weight:700;color:var(--ink);line-height:1.2}
.main-nav{position:absolute;top:55px;left:409px;display:flex;align-items:center;font-size:13px;color:var(--ink);text-transform:uppercase}
.main-nav a{color:inherit;text-decoration:none;margin-right:29px}
.btn{display:inline-block;background:var(--gold);color:var(--white);text-transform:uppercase;font-weight:700;font-size:13px;text-align:center;text-decoration:none}
.nav-donate{width:101px;height:28px;line-height:28px;margin-left:5px}

/* hero */
.hero{position:absolute;top:105px;left:0;width:1200px;height:553px;
  background:radial-gradient(ellipse at 78% 15%,#f2c56a 0%,#d08a3a 25%,transparent 55%),
  linear-gradient(180deg,#b57a3c 0%,#7a4e2a 55%,#4b3624 100%)}
.hero-title{position:absolute;left:128px;top:75px;color:var(--white);font-size:58px;font-weight:800;letter-spacing:2px;line-height:1}
.hero-sub{position:absolute;left:128px;top:145px;color:var(--white);font-size:36px;font-weight:700;line-height:50px;text-transform:uppercase}
.hero-text{position:absolute;left:128px;top:278px;width:545px;color:var(--white);font-size:14px;line-height:20px}
.hero-btn{position:absolute;left:128px;top:457px;width:123px;height:29px;line-height:29px;font-size:12px}

/* sections */
.section-title{position:absolute;left:0;width:1200px;text-align:center;font-size:22px;font-weight:700;color:var(--ink);text-transform:uppercase}
.section-lead{position:absolute;left:150px;width:900px;text-align:center;font-size:13px;line-height:18px}
.mission{position:absolute;top:658px;left:0;width:1200px;height:522px;background:var(--cream)}
.pillar{position:absolute;top:240px;width:300px;text-align:center}
.pillar-icon{width:100px;height:100px;margin:0 auto;border-radius:50%;background:var(--gold);display:flex;align-items:center;justify-content:center}
.pillar-title{margin-top:36px;font-size:18px;font-weight:700;color:var(--ink);text-transform:uppercase}
.pillar-text{margin-top:6px;font-size:13px;line-height:18px;padding:0 10px}

.achievements{position:absolute;top:1180px;left:0;width:1200px;height:785px;background:var(--white)}
.card{position:absolute;top:228px;width:304px}
.card-photo{height:219px}
.card-title{margin-top:34px;font-size:18px;font-weight:600;color:var(--gold);text-transform:uppercase;letter-spacing:.5px}
.card-rule{width:50px;height:2px;background:#ccc;margin:10px 0 12px}
.card-text{font-size:13px;line-height:20px;text-align:justify}
.card-more{margin-top:16px;font-size:14px;color:var(--ink);text-transform:uppercase}

.photo-band{position:absolute;top:1965px;left:0;width:1200px;height:390px;
  background:radial-gradient(ellipse at 55% 75%,#c9a77a 0%,transparent 35%),linear-gradient(135deg,#5a3a24 0%,#8c6a4a 40%,#6a4a30 70%,#3e2818 100%)}

.support{position:absolute;top:2355px;left:0;width:1200px;height:313px;background:var(--cream)}
.support-btn{position:absolute;left:552px;top:210px;width:98px;height:28px;line-height:28px;font-size:12px}

/* footer */
.site-footer{position:absolute;top:2668px;left:0;width:1200px;height:259px;background:var(--footer);color:var(--footer-text)}
.footer-col{position:absolute;top:45px}
.footer-col h4{font-size:14px;font-weight:600;text-transform:uppercase;color:var(--white)}
.footer-col .rule{width:100px;height:1px;background:#6d6862;margin:8px 0 10px}
.footer-col ul{list-style:none;font-size:12px;line-height:15px}
.footer-col p{font-size:12px;line-height:15px;width:290px}
.newsletter-form{display:flex;margin-top:28px}
.newsletter-input{width:204px;height:36px;background:var(--white);font-size:11px;color:#999;padding:11px 8px}
.newsletter-send{width:85px;height:36px;line-height:36px;background:var(--send);color:var(--white);font-weight:700;font-size:13px;text-align:center}
.footer-bottom{position:absolute;top:2927px;left:0;width:1200px;height:83px;background:var(--footer-bottom);color:var(--footer-text);font-size:11px}
.copyright{position:absolute;left:130px;top:36px;text-transform:uppercase}
.copyright span{color:var(--gold)}
.legal{position:absolute;left:617px;top:36px;text-transform:uppercase;word-spacing:2px}
.legal span{margin-right:12px}
.social{position:absolute;left:928px;top:31px;display:flex;gap:12px}
.social i{display:block;width:20px;height:20px;border-radius:50%;background:#d9d5cc}
</style>
</head>
<body>

<header class="site-header">
  <div class="brand-name">Talveth</div>
  <nav class="main-nav">
    <a href="#">About us</a><a href="#">Hunting ethics</a><a href="#">Conservation</a><a href="#">Get involved</a><a href="#">Contact us</a>
    <a href="#" class="btn nav-donate">Donate</a>
  </nav>
</header>

<section class="hero" role="img" aria-label="Stag with large antlers standing in a frosty meadow at golden sunrise">
  <h1 class="hero-title">TALVETH</h1>
  <h2 class="hero-sub">Protect the heritage<br>of hunting</h2>
  <p class="hero-text">Lorem ipsum dolor sit amet voluptatem fugit aut illo omnis explicabo ipsa nemo enim ipsam quasi illo dolores ut voluptatem perspiciatis beatae magni architecto odit aspernatur magni quae aperiam aut veritatis beatae eos aut voluptas doloremque perspiciatis error natus natus, qui aut eaque inventore aut quasi consequuntur consequuntur ipsa</p>
  <a href="#" class="btn hero-btn">Learn more</a>
</section>

<section class="mission">
  <h2 class="section-title" style="top:88px">Help us protect the future of hunting</h2>
  <p class="section-lead" style="top:135px">Lorem ipsum dolor sit amet voluptatem fugit aut illo omnis explicabo ipsa, nemo enim ipsam quasi illo dolores ut voluptatem doloremque perspiciatis beatae magni architecto odit odit, aspernatur magni quae aperiam aut veritatis beatae eos aut voluptas doloremque perspiciatis</p>

  <div class="pillar" style="left:126px">
    <div class="pillar-icon">
      <svg width="50" height="56" viewBox="0 0 50 56"><rect x="6" y="4" width="30" height="40" rx="2" fill="#fff"/><rect x="12" y="12" width="18" height="3" fill="#a39a6a"/><rect x="12" y="19" width="18" height="3" fill="#a39a6a"/><rect x="12" y="26" width="12" height="3" fill="#a39a6a"/><circle cx="36" cy="38" r="9" fill="#fff" stroke="#a39a6a" stroke-width="3"/><path d="M31 45 L29 54 L36 50 L43 54 L41 45Z" fill="#fff"/></svg>
    </div>
    <div class="pillar-title">Hunting ethics</div>
    <p class="pillar-text">Ipsum ipsa odit aperiam aspernatur veritatis unde enim accusantium laudantiu</p>
  </div>
  <div class="pillar" style="left:450px">
    <div class="pillar-icon">
      <svg width="54" height="58" viewBox="0 0 54 58"><circle cx="27" cy="22" r="16" fill="#fff"/><circle cx="15" cy="28" r="11" fill="#fff"/><circle cx="39" cy="28" r="11" fill="#fff"/><rect x="24" y="34" width="6" height="20" fill="#fff"/></svg>
    </div>
    <div class="pillar-title">Conservation</div>
    <p class="pillar-text">Ipsum ipsa odit aperiam aspernatur veritatis unde enim accusantium laudantiu</p>
  </div>
  <div class="pillar" style="left:774px">
    <div class="pillar-icon">
      <svg width="56" height="50" viewBox="0 0 56 50"><path d="M6 18 L20 18 L44 6 L44 40 L20 28 L6 28Z" fill="#fff"/><rect x="12" y="28" width="8" height="14" fill="#fff"/><path d="M48 14 Q54 23 48 32" stroke="#fff" stroke-width="3" fill="none"/></svg>
    </div>
    <div class="pillar-title">Get involved</div>
    <p class="pillar-text">Ipsum ipsa odit aperiam aspernatur veritatis unde enim accusantium laudantiu</p>
  </div>
</section>

<section class="achievements">
  <h2 class="section-title" style="top:88px">What we have done</h2>
  <p class="section-lead" style="top:138px">Lorem ipsum dolor sit amet voluptatem fugit aut illo omnis explicabo ipsa, nemo enim ipsam quasi illo dolores ut voluptatem doloremque perspiciatis beatae magni architecto odit odit, aspernatur magni quae aperiam aut veritatis beatae eos aut voluptas doloremque perspiciatis</p>

  <article class="card" style="left:128px">
    <div class="card-photo" role="img" aria-label="Whitetail deer buck standing in tall autumn grass" style="background:linear-gradient(160deg,#7d7565,#a08a6e 50%,#6e5e4e)"></div>
    <h3 class="card-title">Voluptatem fugit</h3><div class="card-rule"></div>
    <p class="card-text">Lorem ipsum dolor sit amet voluptatem fugit illo omnis explicabo ipsa odit nemo rem ipsam quasi illo dolores ut voluptate odit doloremque perspiciatis beatae magni architecto odit quae aspernatur magni quae aperiam veritatis error.</p>
    <div class="card-more">Read more</div>
  </article>
  <article class="card" style="left:449px">
    <div class="card-photo" role="img" aria-label="Two hunters with a dog walking across an open field" style="background:linear-gradient(180deg,#b8b2a4,#8e8470 55%,#6a5d48)"></div>
    <h3 class="card-title">Sed enim accusantium</h3><div class="card-rule"></div>
    <p class="card-text">Lorem ipsum dolor sit amet voluptatem fugit illo omnis explicabo ipsa odit nemo rem ipsam quasi illo dolores ut voluptate odit doloremque perspiciatis beatae magni architecto odit quae aspernatur magni quae aperiam veritatis error.</p>
    <div class="card-more">Read more</div>
  </article>
  <article class="card" style="left:768px">
    <div class="card-photo" role="img" aria-label="Hunters in camouflage setting up netting among birch trees" style="background:linear-gradient(180deg,#c9c4b8,#7e7260 55%,#5a4c3a)"></div>
    <h3 class="card-title">Aut illo aut veritatis</h3><div class="card-rule"></div>
    <p class="card-text">Lorem ipsum dolor sit amet voluptatem fugit illo omnis explicabo ipsa odit nemo rem ipsam quasi illo dolores ut voluptate odit doloremque perspiciatis beatae magni architecto odit quae aspernatur magni quae aperiam veritatis error.</p>
    <div class="card-more">Read more</div>
  </article>
</section>

<section class="photo-band" role="img" aria-label="Hunting knife, old map and brass compass on burlap"></section>

<section class="support">
  <h2 class="section-title" style="top:70px">Support us as we empower the modern hunter</h2>
  <p class="section-lead" style="top:120px;left:128px;width:944px">Lorem ipsum dolor sit amet voluptatem fugit aut illo omnis explicabo ipsa nemo rem ipsam quasi illo dolores ut voluptatem doloremque perspiciatis beatae magni architecto odit aspernatur magni quae aperiam aut veritatis beatae eos aut voluptas doloremque perspiciatis error natus natusquia ratione ratione dolores consequuntur ut consequuntur perspiciatis architecto sunt beatae architecto aperiam natus</p>
  <a href="#" class="btn support-btn">Donate</a>
</section>

<footer>
  <div class="site-footer">
    <div class="footer-col" style="left:130px"><h4>Company</h4><div class="rule"></div>
      <ul><li>Who we are</li><li>What we do</li><li>Company profile</li><li>What they say</li><li>Our awesome team</li></ul></div>
    <div class="footer-col" style="left:306px"><h4>Address</h4><div class="rule"></div>
      <ul><li>Ridgeline Point</li><li>Tower 8</li><li>128 Floors</li><li>Kestrel Plaza</li><li>Kestrel Road</li><li>Australia</li></ul></div>
    <div class="footer-col" style="left:462px"><h4>Support</h4><div class="rule"></div>
      <ul><li>Forum</li><li>FAQ</li><li>Contact</li><li>Chat</li><li>Find Job</li></ul></div>
    <div class="footer-col" style="left:617px"><h4>Other links</h4><div class="rule"></div>
      <ul><li>Chirpline</li><li>Campfire</li><li>Pinboardly</li><li>Trailspot</li><li>Lodgetalk</li></ul></div>
    <div class="footer-col" style="left:783px"><h4>Newsletter</h4><div class="rule"></div>
      <p>Lorem ipsum dolor sit amet voluptatem fugit illo omnis explicabo ipsa odit nemo rem ipsum</p>
      <div class="newsletter-form"><div class="newsletter-input">enter your email</div><div class="newsletter-send">SEND</div></div></div>
  </div>
  <div class="footer-bottom">
    <div class="copyright">Copyright © 2015 <span>Company</span>. All rights reserved.</div>
    <div class="legal"><span>Term and use</span><span>Privacy policy</span><span>Career</span></div>
    <div class="social"><i></i><i></i><i></i><i></i><i></i></div>
  </div>
</footer>

</body>
</html>
```